elearning course template

Our company has a variety of elearning courses. We are currently redesigning the courses and are looking for a new layout for the online learning courses. The layout should be 800x600 and it needs to incorporate the following elements:
1. Course Name
2. Chapter Name
3. Page name
4. Our company logo (see attached file)
5. Navigation bar that includes:
- Next / back buttons
- Page count
- Audio control bar (see attached file)
- Menu items that include: "Menu, Transcript, Resources"
9. Exit button (may be included on the navigation bar if appropriate)
10. Content area must be 775 wide x 442 high

We would like to see designs that use our company colors, blue (RGB 0,69,144) and orange (RGB 222, 111, 51) and dark gray. We're looking for a solution that is clean, crisp and very user friendly. We'd also like to see a little dimension in the layout, we feel that our current layout is very "flat".

You can find out more about our company at www.fenlark-vro.com.

Industry/Entity Type

Graphic Design

```html
<!DOCTYPE html>
<html lang="en">
<head>
<meta charset="utf-8">
<title>Fenlark eLearning Course Template</title>
<link href="https://fonts.googleapis.com/css2?family=Lato:wght@400;700;900&display=swap" rel="stylesheet">
<style>
  :root {
    --brand-blue: rgb(0, 69, 144);
    --brand-orange: rgb(222, 111, 51);
    --orange-dark: #b8542a;
    --frame-gray: #3b3b3b;
    --bar-light: #dedede;
    --bar-mid: #c9c9c9;
    --track-gray: #8e8e8e;
    --text-gray: #555555;
    --white: #ffffff;
  }
  * { box-sizing: border-box; margin: 0; padding: 0; }
  html, body {
    width: 1200px; height: 900px; overflow: hidden;
    background: var(--frame-gray);
    font-family: "Lato", sans-serif;
  }
  .player {
    position: absolute; left: 0; top: 0;
    width: 800px; height: 600px;
    transform: scale(1.5); transform-origin: 0 0;
    background: var(--frame-gray);
  }
  .header {
    position: absolute; left: 3px; top: 8px; width: 794px; height: 63px;
    background: linear-gradient(#0b4d97, var(--brand-blue));
  }
  .breadcrumb {
    position: absolute; left: 3px; top: 71px; width: 794px; height: 23px;
    background: linear-gradient(#e6773b, var(--brand-orange));
    color: var(--white); font-size: 12px; line-height: 23px; padding-left: 68px;
    box-shadow: 0 2px 3px rgba(0,0,0,.25);
  }
  .brand-peel { position: absolute; left: 3px; top: 8px; width: 145px; height: 100px; }
  .brand-name {
    position: absolute; left: 12px; top: 20px;
    font-weight: 900; font-size: 17px; color: var(--brand-blue);
  }
  .exit-button {
    position: absolute; left: 762px; top: 17px; width: 27px; height: 24px;
    background: linear-gradient(#ffffff, #e4e4e4); border-radius: 3px;
    box-shadow: 0 1px 2px rgba(0,0,0,.4);
  }
  .content-area {
    position: absolute; left: 3px; top: 94px; width: 794px; height: 453px;
    background: var(--white);
  }
  .seek-track {
    position: absolute; left: 3px; top: 547px; width: 495px; height: 4px;
    background: var(--track-gray);
  }
  .seek-fill { width: 245px; height: 100%; background: var(--brand-orange); }
  .time-tip {
    position: absolute; left: 62px; top: 526px; width: 37px; height: 17px;
    background: var(--white); border: 1px solid #cfcfcf; border-radius: 2px;
    font-size: 11px; font-weight: 700; color: #444; text-align: center; line-height: 15px;
  }
  .nav-bar {
    position: absolute; top: 551px; height: 46px;
    background: linear-gradient(var(--bar-light), var(--bar-mid));
  }
  .nav-bar.playback { left: 3px; width: 495px; }
  .nav-bar.course-tools { left: 503px; width: 294px; top: 547px; height: 50px; }
  .knob {
    position: absolute; width: 12px; height: 12px; border-radius: 50%;
    background: radial-gradient(circle at 50% 50%, var(--brand-orange) 2px, #f4f4f4 3px, #cfcfcf 6px);
    box-shadow: 0 1px 2px rgba(0,0,0,.4);
  }
  .volume-track {
    position: absolute; left: 88px; top: 573px; width: 160px; height: 4px; border-radius: 2px;
    background: #bdbdbd; box-shadow: inset 0 1px 1px rgba(0,0,0,.25);
  }
  .volume-fill { width: 103px; height: 100%; border-radius: 2px; background: var(--brand-orange); }
  .divider { position: absolute; left: 313px; top: 558px; width: 1px; height: 32px; background: #8a8a8a; }
  .page-button {
    position: absolute; top: 557px; width: 34px; height: 34px; border-radius: 50%;
    box-shadow: 0 1px 3px rgba(0,0,0,.45);
  }
  .page-button.back { left: 341px; background: linear-gradient(#fafafa, #d6d6d6); }
  .page-button.next { left: 439px; background: linear-gradient(#ea7f45, var(--orange-dark)); }
  .page-button svg { display: block; }
  .page-count {
    position: absolute; left: 380px; top: 566px; width: 56px; text-align: center;
    font-size: 12px; color: #333;
  }
  .page-count .total { color: var(--text-gray); }
  .tool-button {
    position: absolute; height: 37px; border-radius: 3px;
    font-size: 12px; text-align: center; line-height: 37px;
    box-shadow: 0 1px 3px rgba(0,0,0,.4);
    background: linear-gradient(#ea7f45, #cc5e2b); color: var(--white);
    border: 1px solid #a9491f;
  }
  .tool-button.active {
    background: linear-gradient(#ffffff, #e8e8e8); color: var(--brand-orange);
    border: 1px solid #bdbdbd;
  }
  .menu-item { left: 520px; width: 84px; }
</style>
</head>
<body>
<main class="player">
  <header class="header"></header>
  <div class="breadcrumb">Course Name- Chapter Name - Page name</div>

  <svg class="brand-peel" viewBox="0 0 145 100" aria-hidden="true">
    <defs>
      <linearGradient id="fold" x1="0" y1="1" x2="1" y2="0">
        <stop offset="0" stop-color="#9a9a9a"/>
        <stop offset=".5" stop-color="#f4f4f4"/>
        <stop offset="1" stop-color="#ffffff"/>
      </linearGradient>
    </defs>
    <path d="M0 0 H138 Q80 30 40 62 Q20 78 0 80 Z" fill="#ffffff"/>
    <path d="M138 0 Q80 30 40 62 Q20 78 0 80 Q30 92 50 90 Q70 60 138 0 Z" fill="url(#fold)" opacity=".9"/>
  </svg>
  <div class="brand-name">Fenlark</div>

  <div class="exit-button" aria-label="Exit course">
    <svg width="27" height="24" viewBox="0 0 27 24"><path d="M9 7 L18 17 M18 7 L9 17" stroke="var(--brand-orange)" stroke-width="2.6" stroke-linecap="round"/></svg>
  </div>

  <section class="content-area"></section>

  <div class="nav-bar playback"></div>
  <div class="nav-bar course-tools"></div>

  <div class="seek-track"><div class="seek-fill"></div></div>
  <div class="knob" style="left:242px;top:543px"></div>
  <div class="time-tip">0:20</div>

  <svg style="position:absolute;left:65px;top:564px" width="20" height="18" viewBox="0 0 20 18" aria-label="Volume">
    <path d="M1 6 H5 L11 1 V17 L5 12 H1 Z" fill="var(--brand-orange)"/>
    <path d="M14 5 Q17 9 14 13" stroke="var(--brand-orange)" stroke-width="1.6" fill="none"/>
  </svg>
  <div class="volume-track"><div class="volume-fill"></div></div>
  <div class="knob" style="left:185px;top:569px"></div>

  <div class="divider"></div>

  <div class="page-button back" aria-label="Previous page">
    <svg width="34" height="34" viewBox="0 0 34 34"><path d="M20 12 L13 17 L20 22 Z" fill="var(--brand-orange)"/></svg>
  </div>
  <div class="page-count">2 / <span class="total">10</span></div>
  <div class="page-button next" aria-label="Next page">
    <svg width="34" height="34" viewBox="0 0 34 34"><path d="M14 12 L21 17 L14 22 Z" fill="#ffffff"/></svg>
  </div>

  <div class="tool-button menu-item" style="top:440px">Item 3</div>
  <div class="tool-button menu-item" style="top:478px">Item 2</div>
  <div class="tool-button menu-item" style="top:516px">Item 1</div>

  <div class="tool-button active" style="left:524px;top:555px;width:75px">Menu</div>
  <div class="tool-button" style="left:617px;top:555px;width:74px">Transcript</div>
  <div class="tool-button" style="left:709px;top:555px;width:74px">Resources</div>
</main>
</body>
</html>
```